Halvik Denatl Laboratory nees a window design

We want to make a window cover 8 feet wide and 6 feet tall to advertise our dental lab with all the products we produce<br/>: Digital Cad/Cam<br/>: Implants<br/>: Dentures<br/>: Cast Partials <br/>: Orthodontic appliances<br/><br/> and it has to include a service we provide for a denturist on site by appointment only.<br/><br/>Please use the sample logo below our colours are white backround and blue letters

Font styles to use
Script

Colors
ffffff
0355a3

Requirements
Nice to have
• a picture of a teddy bear on a dental chair, or some dental work particularly bridge work since our moto is Building bridges since 1976
Should not have
• real people

```html
<!DOCTYPE html>
<html lang="en">
<head>
<meta charset="UTF-8">
<title>Halvik Dental Laboratory – Window Banner</title>
<link href="https://fonts.googleapis.com/css2?family=Crimson+Pro:wght@400;700&display=swap" rel="stylesheet">
<style>
  :root {
    --backdrop: #231f20;
    --white: #ffffff;
    --brand-blue: #0355a3;
    --pill-blue: #034a91;
    --logo-blue: #1b86cc;
    --tooth-light: #f4f4f4;
    --tooth-shade: #cfcfcf;
  }
  * { margin: 0; padding: 0; box-sizing: border-box; }
  html, body {
    width: 1200px;
    height: 1200px;
    overflow: hidden;
    background: var(--backdrop);
  }
  .canvas {
    position: relative;
    width: 1200px;
    height: 1200px;
  }
  .banner {
    position: absolute;
    left: 51px;
    top: 327px;
    width: 1097px;
    height: 549px;
    background: var(--white);
    overflow: hidden;
    font-family: "Crimson Pro", Georgia, serif;
  }
  .banner-shapes {
    position: absolute;
    inset: 0;
  }
  .tooth-illustration {
    position: absolute;
    left: 55px;
    top: 75px;
    width: 288px;
    height: 419px;
    border-radius: 140px 140px 60px 60px;
    background: radial-gradient(ellipse at 45% 35%, var(--tooth-light) 0%, #e6e6e6 55%, var(--tooth-shade) 100%);
  }
  .brand-name {
    position: absolute;
    left: 420px;
    top: 62px;
    width: 640px;
    text-align: center;
    color: var(--logo-blue);
    font-weight: 400;
    line-height: 1;
  }
  .brand-name .brand-main {
    display: block;
    font-size: 82px;
    letter-spacing: 3px;
    text-transform: uppercase;
  }
  .brand-name .brand-sub {
    display: block;
    font-size: 40px;
    margin-top: 6px;
    letter-spacing: 1px;
  }
  .service-list {
    position: absolute;
    left: 420px;
    top: 235px;
    width: 640px;
    text-align: center;
    color: var(--brand-blue);
    font-weight: 700;
    font-size: 41px;
    line-height: 52px;
    letter-spacing: -0.5px;
    text-transform: uppercase;
  }
  .denturist-pill {
    position: absolute;
    left: 523px;
    top: 427px;
    width: 434px;
    height: 66px;
    border-radius: 33px;
    background: var(--pill-blue);
    color: var(--white);
    text-align: center;
    text-transform: uppercase;
    padding-top: 4px;
  }
  .denturist-pill .pill-title {
    display: block;
    font-weight: 700;
    font-size: 31px;
    line-height: 32px;
  }
  .denturist-pill .pill-note {
    display: block;
    font-weight: 400;
    font-size: 19px;
    line-height: 22px;
    letter-spacing: 0.3px;
  }
</style>
</head>
<body>
<div class="canvas">
  <section class="banner">
    <svg class="banner-shapes" width="1097" height="549" viewBox="0 0 1097 549" aria-hidden="true">
      <polygon points="0,74 40,38 572,549 0,549" fill="var(--brand-blue)"/>
      <polygon points="960,0 1097,0 1097,74 1067,102" fill="var(--brand-blue)"/>
    </svg>

    <div class="tooth-illustration" role="img" aria-label="Glossy white 3D molar tooth illustration"></div>

    <h1 class="brand-name">
      <span class="brand-main">Halvik</span>
      <span class="brand-sub">Dental Laboratory</span>
    </h1>

    <p class="service-list">
      Digital CAD | Implants |<br>
      Dentures | Cast Partials |<br>
      Orthodontic Appliances
    </p>

    <div class="denturist-pill">
      <span class="pill-title">Denturist :</span>
      <span class="pill-note">On site by appointment only</span>
    </div>
  </section>
</div>
</body>
</html>
```